Security Cheat Sheets

We are after a nicely presented easy to follow cheat sheet around security such as Phishing and scams and acceptable use we can send to our clients for awareness.
The example Cheat Sheets is some info we would like (was something i downloaded from the internet so do not copy verbatim but has some good content ideas we would like to use) and a very simple example i prepared plus our logos etc.

```html
<!DOCTYPE html>
<html lang="en">
<head>
<meta charset="utf-8">
<title>Phishing and Scams – Nexora Technology</title>
<link href="https://fonts.googleapis.com/css2?family=Krona+One&family=Montserrat:wght@500;600;700;800&display=swap" rel="stylesheet">
<style>
:root{
  --page:#f2f2f2;
  --navy:#121a4a;
  --navy-deep:#0c1238;
  --blue:#1f86ff;
  --blue-panel:#1f6ff2;
  --blue-line:#3566cf;
  --green:#5fe22a;
  --green-dark:#2f9e12;
  --red:#e3262b;
  --white:#ffffff;
  --ink:#0c1238;
}
*{box-sizing:border-box;margin:0;padding:0}
html,body{width:1200px;height:2270px;overflow:hidden;background:var(--page)}
body{font-family:"Montserrat",sans-serif;color:var(--white);position:relative}
.flyer{position:absolute;left:50px;top:423px;width:1100px;height:1424px;overflow:hidden;
  background:radial-gradient(ellipse 620px 520px at 900px 160px,#1d3c9a 0%,rgba(29,60,154,0) 70%),
  linear-gradient(180deg,#16205a 0%,var(--navy) 45%,var(--navy-deep) 100%);
  box-shadow:0 30px 60px rgba(0,0,0,.35)}
.abs{position:absolute}
.hero-art{left:700px;top:0;width:400px;height:360px;
  background:radial-gradient(ellipse 160px 190px at 210px 190px,#3ff3ff 0%,#1aa6e6 40%,rgba(26,120,230,0) 75%)}
.brand{left:58px;top:60px;display:flex;align-items:center;gap:14px}
.brand-mark{width:48px;height:48px;background:var(--blue)}
.brand-name{font-weight:600;font-size:26px;letter-spacing:.5px;color:var(--white)}
.brand-tag{left:128px;top:104px;font-size:14px;font-weight:500;letter-spacing:1px}
.title{left:54px;font-family:"Krona One",sans-serif;font-size:78px;line-height:.9;letter-spacing:-1px}
.title-a{top:166px;color:var(--blue)}
.title-b{top:240px;color:var(--white)}
.topics{left:53px;top:325px;width:983px;height:44px;background:var(--green);border-radius:6px;
  display:flex;align-items:center;color:var(--ink);font-weight:700;font-size:25px}
.topic{display:flex;align-items:center;gap:10px;padding:0 18px;border-right:2px solid rgba(12,18,56,.25);height:30px}
.topic:last-child{border-right:none}
.tick-s{width:18px;height:18px}
.section-title{left:58px;top:390px;font-size:36px;font-weight:800;letter-spacing:.5px}
.section-title .hl{color:var(--blue)}
.tag{left:58px;height:34px;display:flex;align-items:center}
.tag-label{background:var(--green);color:var(--ink);font-weight:700;font-size:22px;height:34px;padding:0 12px;display:flex;align-items:center}
.tag svg{height:34px;width:72px}
.dot{width:14px;height:14px;border-radius:50%;background:var(--blue);border:3px solid #9fc3ff}
.row{left:58px;width:983px;height:58px;border:2px solid var(--blue-line);border-radius:29px;
  display:flex;align-items:center;padding-left:22px;gap:16px;font-size:16.5px;font-weight:500;line-height:1.18}
.icon{width:36px;height:36px;flex:none}
.hacked{left:58px;top:1023px;width:983px;height:156px;border-radius:10px;overflow:hidden;display:flex}
.hacked-half{flex:1;display:flex;align-items:center;padding:0 22px 0 26px;gap:14px;font-size:17px;font-weight:500;line-height:1.18}
.hacked-half.left{background:var(--blue-panel)}
.hacked-half.right{background:#1b5fe6}
.hacked-half p{flex:1}
.hacked-art{width:120px;height:110px;border-radius:8px;flex:none}
.art-a{background:linear-gradient(135deg,#7b5bff,#3a2fb8)}
.art-b{background:linear-gradient(135deg,#e9eefc,#2f6fe0)}
.hacked-label{left:330px;top:1000px;width:440px;height:44px;background:var(--white);color:var(--ink);
  border-radius:8px;display:flex;align-items:center;justify-content:center;font-weight:800;font-size:23px}
.do-title{left:56px;top:1192px;font-size:38px;font-weight:800}
.do-title .hl{color:var(--green)}
.do-text{left:60px;top:1240px;width:700px;font-size:18.5px;font-weight:500;line-height:1.2}
.lock-art{left:820px;top:1175px;width:240px;height:130px;
  background:radial-gradient(ellipse 90px 60px at 170px 65px,#2fa8ff 0%,rgba(31,120,255,.25) 55%,rgba(18,26,74,0) 80%)}
.contact-label{left:60px;top:1300px;font-size:19px;font-weight:800;color:var(--blue)}
.phone{left:58px;top:1328px;display:flex;align-items:center;gap:10px;font-size:38px;font-weight:800}
.contact-line{left:0;top:0;width:1100px;height:1424px;pointer-events:none}
.web{top:1344px;display:flex;align-items:center;gap:9px;font-size:19px;font-weight:700;white-space:nowrap}
.web svg{width:19px;height:19px;flex:none}
</style>
</head>
<body>
<main class="flyer">
  <div class="abs hero-art" role="img" aria-label="Glowing cyan security shield with a keyhole over falling binary code"></div>

  <div class="abs brand"><span class="brand-mark"></span><span class="brand-name">NEXORA TECHNOLOGY</span></div>
  <div class="abs brand-tag">"ICT Solutions &amp; Engineering"</div>

  <h1 class="abs title title-a">PHISHING</h1>
  <div class="abs title title-b">AND SCAMS</div>

  <div class="abs topics">
    <span class="topic"><svg class="tick-s" viewBox="0 0 20 20"><circle cx="10" cy="10" r="9" fill="#fff"/><path d="M5.5 10.5l3 3 6-6" stroke="#2f9e12" stroke-width="2.4" fill="none"/></svg>How to detect?</span>
    <span class="topic"><svg class="tick-s" viewBox="0 0 20 20"><circle cx="10" cy="10" r="9" fill="#fff"/><path d="M5.5 10.5l3 3 6-6" stroke="#2f9e12" stroke-width="2.4" fill="none"/></svg>What to do?</span>
    <span class="topic"><svg class="tick-s" viewBox="0 0 20 20"><circle cx="10" cy="10" r="9" fill="#fff"/><path d="M5.5 10.5l3 3 6-6" stroke="#2f9e12" stroke-width="2.4" fill="none"/></svg>How to avoid being scammed?</span>
  </div>

  <h2 class="abs section-title"><span class="hl">DETECTION AND</span> AWARENESS</h2>

  <div class="abs tag" style="top:443px">
    <span class="tag-label">Look at the senders email address</span>
    <svg viewBox="0 0 72 34"><path d="M0 0h14l16 17-16 17H0l16-17z" fill="#5fe22a"/><path d="M22 0h14l16 17-16 17H22l16-17z" fill="#3fbf1a"/><path d="M44 0h14l16 17-16 17H44l16-17z" fill="#2a8f12"/></svg>
  </div>
  <div class="abs dot" style="left:52px;top:488px"></div>

  <div class="abs row" style="top:497px"><svg class="icon" viewBox="0 0 36 36"><circle cx="18" cy="18" r="17" fill="#5fe22a"/><path d="M10 18.5l5.5 5.5 11-11" stroke="#fff" stroke-width="3.6" fill="none"/></svg>Senders From Email address is from your domain or a trusted domain</div>
  <div class="abs row" style="top:557px"><svg class="icon" viewBox="0 0 36 36"><circle cx="18" cy="18" r="17" fill="#e3262b"/><path d="M12 12l12 12M24 12L12 24" stroke="#fff" stroke-width="3.6"/></svg><span>Senders From Email address is from a random email address or freemail like mailzo<br>or quickpost account</span></div>
  <div class="abs row" style="top:617px"><svg class="icon" viewBox="0 0 36 36"><circle cx="18" cy="18" r="17" fill="#e3262b"/><path d="M12 12l12 12M24 12L12 24" stroke="#fff" stroke-width="3.6"/></svg><span>Senders From Email address is from the CEO / Accounts etc but the address is not your corporate domain<br>for example ceo@mailzo.com</span></div>
  <div class="abs row" style="top:677px"><svg class="icon" viewBox="0 0 36 36"><circle cx="18" cy="18" r="17" fill="#e3262b"/><path d="M12 12l12 12M24 12L12 24" stroke="#fff" stroke-width="3.6"/></svg>Senders From Email address is from a random email address or freemail like mailzo or quickpost account</div>
  <div class="abs row" style="top:737px"><svg class="icon" viewBox="0 0 36 36"><circle cx="18" cy="18" r="17" fill="#e3262b"/><path d="M12 12l12 12M24 12L12 24" stroke="#fff" stroke-width="3.6"/></svg><span>Sender is pretending to be an internal staff member but the email body has the "External Mail" pink<br>bar warning</span></div>

  <div class="abs tag" style="top:815px">
    <span class="tag-label">Contain a link to reset password or Scare Tactic</span>
    <svg viewBox="0 0 72 34"><path d="M0 0h14l16 17-16 17H0l16-17z" fill="#5fe22a"/><path d="M22 0h14l16 17-16 17H22l16-17z" fill="#3fbf1a"/><path d="M44 0h14l16 17-16 17H44l16-17z" fill="#2a8f12"/></svg>
  </div>
  <div class="abs dot" style="left:52px;top:855px"></div>

  <div class="abs row" style="top:864px"><svg class="icon" viewBox="0 0 36 36"><circle cx="18" cy="18" r="17" fill="#e3262b"/><path d="M12 12l12 12M24 12L12 24" stroke="#fff" stroke-width="3.6"/></svg>Vantacore, the bank, the Tax Office and others will not ask you to click a link to reset your password</div>
  <div class="abs row" style="top:924px"><svg class="icon" viewBox="0 0 36 36"><circle cx="18" cy="18" r="17" fill="#e3262b"/><path d="M12 12l12 12M24 12L12 24" stroke="#fff" stroke-width="3.6"/></svg><span>Vantacore, NetGrid and others do not monitor your computer or network and advise you they detected an<br>error click a link to resolve</span></div>
  <div class="abs dot" style="left:1023px;top:976px"></div>

  <section class="abs hacked">
    <div class="hacked-half left"><p>There is a very strong likelihood you were not hacked. Scammers will obtain your email address from websites, careerlink or from numerous methods.</p><div class="hacked-art art-a" role="img" aria-label="Illustration of a laptop with a verified security shield"></div></div>
    <div class="hacked-half right"><p>Scammers are pretending to be someone else (phishing) or use a scare tactic to trick you into giving them your information / passwords or other fraud attempts.</p><div class="hacked-art art-b" role="img" aria-label="Illustration of a laptop with security padlock and fingerprint shield"></div></div>
  </section>
  <div class="abs hacked-label">DOES THIS MEAN I WAS HACKED</div>

  <h2 class="abs do-title"><span class="hl">WHAT SHOULD</span> I DO</h2>
  <p class="abs do-text">You can safely ignore and delete the email and if in doubt, please contact NEXORA who can check and advise further.</p>
  <div class="abs lock-art" role="img" aria-label="Glowing digital padlock inside a circuit ring"></div>

  <svg class="abs contact-line" viewBox="0 0 1100 1424"><path d="M58 1300H322l38 27H1040" stroke="#c9d6ff" stroke-width="1.5" fill="none"/><circle cx="1044" cy="1327" r="5" fill="#1f86ff" stroke="#fff" stroke-width="1.5"/></svg>
  <div class="abs contact-label">CONTACT US</div>
  <div class="abs phone"><svg width="30" height="30" viewBox="0 0 30 30"><circle cx="15" cy="15" r="14" fill="#5fe22a"/><path d="M10 8c1-1 2 0 3 2s0 2-1 3c1 2 3 4 5 5 1-1 1-2 3-1s3 2 2 3c-1 2-3 3-6 1-3-2-6-5-7-8-1-2 0-4 1-5z" fill="#121a4a"/></svg>1300 555 019</div>
  <div class="abs web" style="left:385px"><svg viewBox="0 0 20 20"><circle cx="10" cy="10" r="8.5" stroke="#5fe22a" stroke-width="2" fill="none"/><path d="M1.5 10h17M10 1.5c-4 4-4 13 0 17M10 1.5c4 4 4 13 0 17" stroke="#5fe22a" stroke-width="1.6" fill="none"/></svg>WWW.NEXORA-TECH.COM.AU</div>
  <div class="abs web" style="left:725px"><svg viewBox="0 0 20 20"><rect x="1" y="4" width="18" height="12" fill="#5fe22a"/><path d="M1 4l9 7 9-7" stroke="#121a4a" stroke-width="1.6" fill="none"/></svg>HELP@NEXORA-TECH.COM.AU</div>
</main>
</body>
</html>
```